Re-design of current business cards

We are updating our website with new colors and layout. Would like to re-design our business cards to co-ordinate. See attached pdf with new Brindlecraft website colors. We would also like to combine our 2 brands on the one business card. Attached is the new design for our Brindlecraft website, current business cards, which are one sided, brindlecraft logo in tiff, .ai for fonts. Brindlecraft logo font is Optimum, Quillmarsh website home page image, Quillmarsh brand statics for products which includes the logo for this brand.

Quillmarsh brand will stay the dark gray on the website. See attached statics for product and website home page.
Updates

The business cards will be 2 sided. Brindlecraft Brand on one side and Quillmarsh Brand on the other. The colors for Brindlecraft need to follow the color scheme of the brindlecraft website pdf I uploaded. The colors are a blue, lighter teal blue and white. Quillmarsh needs to follow the dark gray color on files uploaded

Target Market(s)

The trade and consumers

Industry/Entity Type

Home Furnishing

Contact Information for Business Card

We are updating our website with new colors and layout. Would like to re-design our business cards to co-ordinate. We would also like to combine our 2 brands onto 1 2 sided business cards.

Requirements
Must have
• Colors that match our new website, see attached image.
• RGB colors
• navy -#152842
• teal - 98aeb9
• The gray color used for Quillmarsh brands.
• ll logos and fonts should stay the same.

```html
<!DOCTYPE html>
<html lang="en">
<head>
<meta charset="utf-8">
<title>Brindlecraft / Quillmarsh business card</title>
<link href="https://fonts.googleapis.com/css2?family=Lato:wght@400;700&display=swap" rel="stylesheet">
<style>
  :root {
    --backdrop: #a9bcc4;
    --card-light: #f0f0ee;
    --card-dark: #3b3b3b;
    --navy: #152842;
    --teal: #98aeb9;
    --ink: #152842;
    --ink-muted: #4a5a6e;
    --ink-on-dark: #cfcfcd;
    --tagline-on-dark: #9b9b99;
  }
  * { box-sizing: border-box; margin: 0; padding: 0; }
  html, body { width: 1200px; height: 983px; overflow: hidden; }
  body {
    background: var(--backdrop);
    font-family: "Lato", Arial, sans-serif;
    display: flex;
    align-items: center;
    justify-content: center;
    gap: 44px;
  }
  .card {
    width: 520px;
    height: 297px;
    position: relative;
    box-shadow: 0 10px 24px rgba(40, 60, 70, 0.25);
  }

  /* Brindlecraft side */
  .card--brindlecraft { background: var(--card-light); color: var(--ink); }
  .brand-lockup {
    position: absolute; left: 38px; top: 40px;
    display: flex; align-items: center; gap: 12px;
  }
  .brand-name {
    font-size: 27px; font-weight: 400; letter-spacing: 2px; color: var(--navy);
  }
  .brand-dot {
    width: 24px; height: 24px; border-radius: 50%; background: var(--teal);
  }
  .brand-rule {
    position: absolute; left: 38px; top: 84px;
    width: 444px; height: 2px; background: var(--teal);
  }
  .address {
    position: absolute; left: 38px; top: 100px;
    font-size: 12.5px; line-height: 1.4; color: var(--navy);
  }
  .address .web { margin-top: 6px; }
  .person {
    position: absolute; left: 290px; top: 150px;
  }
  .person-name {
    font-size: 15px; font-weight: 700; letter-spacing: 0.5px;
    color: var(--navy); text-transform: uppercase;
  }
  .person-title { font-size: 11.5px; margin-top: 2px; color: var(--ink-muted); }
  .phones {
    position: absolute; left: 290px; top: 206px;
    font-size: 12px; line-height: 1.35; color: var(--navy);
  }
  .phones .label { color: var(--ink-muted); }
  .phones .number { margin-bottom: 6px; }

  /* Quillmarsh side */
  .card--quillmarsh { background: var(--card-dark); }
  .quill-name {
    position: absolute; left: 60px; top: 112px;
    font-size: 42px; font-weight: 400; letter-spacing: 4px;
    color: var(--ink-on-dark); text-transform: uppercase;
  }
  .quill-tagline {
    position: absolute; left: 62px; top: 186px;
    font-size: 13px; letter-spacing: 0.6px; color: var(--tagline-on-dark);
  }
</style>
</head>
<body>
  <section class="card card--brindlecraft" aria-label="Brindlecraft side">
    <div class="brand-lockup">
      <span class="brand-name">BRINDLECRAFT</span>
      <span class="brand-dot"></span>
    </div>
    <div class="brand-rule"></div>
    <div class="address">
      <p>PO Box 412/1870, Larkspur Hill RD</p>
      <p>Fenwick Falls, OREGON 97301</p>
      <p class="web">dwhitcombe@brindlecraft.com</p>
      <p>www.brindlecraft.com</p>
    </div>
    <div class="person">
      <p class="person-name">Dana Whitcombe</p>
      <p class="person-title">Graphic | Photography Director</p>
    </div>
    <div class="phones">
      <p class="label">mobile</p>
      <p class="number">555.210.4418</p>
      <p class="label">fax</p>
      <p class="number">555.210.4472</p>
    </div>
  </section>

  <section class="card card--quillmarsh" aria-label="Quillmarsh side">
    <p class="quill-name">Quillmarsh</p>
    <p class="quill-tagline">Discover the luxury of home.</p>
  </section>
</body>
</html>
```